Professional business card for an Actor

I'd like a professional business card I could give out to producers, and casting directors when meeting at an event. Here is the info I would like to have on my business card.

I am not sure 100% of what I want or how I want it so I am open to suggestions. I know I want something minimalistic. Clean. Straight forward. Something to make them want to find out more about me.

Here is what I'd want to be on the card:

- Full name: Tomas Velbrik (Maybe job: Actor or International Actor)
- My headshot photo is attached but I'm happy to see other options (You can find more photos in the gallery on my webpage www.tovelbrik.net but it should be a headshot)
- Webpage: www.tovelbrik.net (Perhaps a QR code to my site would be great??)
- Snapgrid username.
- Email
- Mobile number (with ChatLoop)

Optional/ideas:

- Languages spoken? English, Spanish, Galician, French, Portuguese.
- QR code to my showreel: https://reelhost.example/518204736
- Castfolio profile https://app.castfolio.example/5207-1938-4462 (QR code???)

The design of the business card should be clean and uncluttered, avoiding an excess of elements, or at least, well structured. I am just giving many ideas but I trust you to translate it into the card :)

- Style minimalistic but It could be something arty too. Whatever that means!

THANK YOU so much!!!!!
Updates

Nice to have

UPDATE: Thank you everyone for your submissions. Just for inspiration if this helps, I like some of the styles than can be found here: https://www.pinboardly.example/CardIdeasHub/performer-card-layouts/ Also. I would also be happy to see a version with Letterpress, Embossed printing or Thermorelief (See atttached images)

Should not have

UPDATE2: Please no white backgrounds. Great work everyone. I would suggest something like the style attached in the latest files. A reference for the style not the colours. THANK YOU!!!

Contact Information for Business Card

Details mentioned in the project description.

Requirements
Nice to have
• UPDATE: Thank you everyone for your submissions. Just for inspiration if this helps, I like some of the styles than can be found here: https://www.pinboardly.example/CardIdeasHub/performer-card-layouts/ Also. I would also be happy to see a version with Letterpress, Embossed printing or Thermorelief (See atttached images)
Should not have
• UPDATE2: Please no white backgrounds. Great work everyone. I would suggest something like the style attached in the latest files. A reference for the style not the colours. THANK YOU!!!

```html
<!DOCTYPE html>
<html lang="en">
<head>
<meta charset="utf-8">
<title>Tomas Velbrik – Business Cards</title>
<link rel="stylesheet" href="https://fonts.googleapis.com/css2?family=Exo+2:wght@300;700&family=Questrial&display=swap">
<style>
  :root {
    --canvas: #ffffff;
    --olive: #bcbb4f;
    --paper: #ffffff;
    --ink: #1d1d1b;
    --photo-light: #3a3a30;
    --photo-dark: #151513;
    --outline: #2a2a2a;
  }
  * { box-sizing: border-box; margin: 0; padding: 0; }
  html, body { width: 900px; height: 1200px; overflow: hidden; background: var(--canvas); }
  .canvas { position: relative; width: 900px; height: 1200px; }

  .card {
    position: absolute;
    top: 306px;
    width: 340px;
    height: 587px;
    border: 1px solid var(--outline);
    overflow: hidden;
  }
  .card--olive { left: 80px; }
  .card--white { left: 480px; }

  .card__art { position: absolute; inset: 0; width: 100%; height: 100%; }

  .card__name {
    position: absolute; left: 122px; top: 318px;
    font-family: "Exo 2", sans-serif; font-weight: 700;
    font-size: 22px; letter-spacing: 0.5px; color: var(--ink);
    white-space: nowrap;
  }
  .card__role {
    position: absolute; left: 121px; top: 346px;
    font-family: "Exo 2", sans-serif; font-weight: 300;
    font-size: 17px; line-height: 22px; letter-spacing: 2.6px;
    text-transform: uppercase;
  }
  .card__contact {
    position: absolute; left: 118px; top: 422px;
    font-family: "Questrial", sans-serif;
    font-size: 16.5px; line-height: 21px; color: var(--ink);
    white-space: nowrap;
  }
  .card__follow {
    position: absolute; left: 119px; top: 492px;
    font-family: "Questrial", sans-serif;
    font-size: 13px; letter-spacing: 0.3px;
  }
  .card__social {
    position: absolute; left: 119px; top: 516px;
    display: flex; gap: 10px;
    font-family: "Questrial", sans-serif; font-size: 12px;
  }
  .card__social-item { display: flex; align-items: center; gap: 4px; }
  .card__social-mark { width: 10px; height: 10px; border-radius: 2px; }

  .card--olive .card__role,
  .card--olive .card__follow,
  .card--olive .card__social { color: var(--paper); }
  .card--olive .card__social-mark { background: var(--paper); }

  .card--white .card__role,
  .card--white .card__follow,
  .card--white .card__social { color: var(--olive); }
  .card--white .card__social-mark { background: var(--olive); }
</style>
</head>
<body>
<main class="canvas">

  <section class="card card--olive">
    <svg class="card__art" viewBox="0 0 340 587" preserveAspectRatio="none">
      <defs>
        <linearGradient id="headshot-olive" x1="0" y1="0" x2="0" y2="1">
          <stop offset="0" stop-color="var(--photo-light)"/>
          <stop offset="1" stop-color="var(--photo-dark)"/>
        </linearGradient>
      </defs>
      <rect width="340" height="587" fill="url(#headshot-olive)" role="img" aria-label="Headshot of the actor against a dark studio backdrop"/>
      <polygon points="108,304 297,304 340,284 340,587 0,587 0,429 108,385" fill="var(--olive)"/>
    </svg>
    <h1 class="card__name">TOMAS VELBRIK</h1>
    <p class="card__role">International<br>Actor</p>
    <p class="card__contact">Tovelbrik@inbox.example<br>www.tovelbrik.net</p>
    <p class="card__follow">FOLLOW @</p>
    <ul class="card__social" style="list-style:none">
      <li class="card__social-item"><span class="card__social-mark"></span>Facepage</li>
      <li class="card__social-item"><span class="card__social-mark"></span>Linkwork</li>
      <li class="card__social-item"><span class="card__social-mark"></span>Snapgrid</li>
    </ul>
  </section>

  <section class="card card--white">
    <svg class="card__art" viewBox="0 0 340 587" preserveAspectRatio="none">
      <defs>
        <linearGradient id="headshot-white" x1="0" y1="0" x2="0" y2="1">
          <stop offset="0" stop-color="var(--photo-light)"/>
          <stop offset="1" stop-color="var(--photo-dark)"/>
        </linearGradient>
      </defs>
      <rect width="340" height="587" fill="url(#headshot-white)" role="img" aria-label="Headshot of the actor against a dark studio backdrop"/>
      <path d="M108,326 Q108,304 130,304 L297,304 L340,284 L340,587 L0,587 L0,429 L108,385 Z" fill="var(--paper)"/>
    </svg>
    <h1 class="card__name">TOMAS VELBRIK</h1>
    <p class="card__role">International<br>Actor</p>
    <p class="card__contact">Tovelbrik@inbox.example<br>www.tovelbrik.net</p>
    <p class="card__follow">FOLLOW @</p>
    <ul class="card__social" style="list-style:none">
      <li class="card__social-item"><span class="card__social-mark"></span>Facepage</li>
      <li class="card__social-item"><span class="card__social-mark"></span>Linkwork</li>
      <li class="card__social-item"><span class="card__social-mark"></span>Snapgrid</li>
    </ul>
  </section>

</main>
</body>
</html>
```